Harvest Gathering event flyer

I would like a church event flyer designed. The event is called "HARVEST GATHERING 2018". I am looking for a professional, yet catchy design that uses our brand colors and logo creatively while communicating key information of the event effectively.

1. The logo is attached in two color formats. The designer has the choice to use them as he/she want.

2. The location of the event is: Lindqvist Community Center, 482 Tamsworth Street, Portland, ME 04102
3. Time and date of event. The designer can organize and format the date and time as he/she pleases.
December 28th, 29th @ 7:00PM
December 30th @ 10:00AM
4. The topic of the event is "Tongues of fire". The designer is free to use this phrase as he/she pleases to create a good composition.
5. Speaker: Prophet Marcus Obuya
6. Contact information: contact@cedarbrookfellowship.org - Telephone number: 207 555 0148

7. I would also like the following three words on the flyer. These words describe the focus of the event: FIRE, REVIVAL, PROPHETIC

```html
<!DOCTYPE html>
<html lang="en">
<head>
<meta charset="utf-8">
<title>Harvest Gathering 2018</title>
<link rel="stylesheet" href="https://fonts.googleapis.com/css2?family=Open+Sans:wght@400;600;700&display=swap">
<style>
  :root {
    --navy-deep: #0d2d4f;
    --navy: #1b4a78;
    --sky: #4d7bab;
    --orange: #f7931e;
    --white: #ffffff;
    --mist: #c9d3de;
    --logo-ink: #1c3b63;
  }
  html, body {
    margin: 0;
    padding: 0;
    overflow: hidden;
    background: var(--navy-deep);
  }
  .flyer {
    position: relative;
    width: 927px;
    height: 1200px;
    overflow: hidden;
    font-family: "Open Sans", Arial, sans-serif;
    color: var(--white);
    background: linear-gradient(180deg, var(--sky) 0%, var(--navy) 40%, var(--navy-deep) 100%);
  }
  .flyer p, .flyer h1 { margin: 0; }
  .hero-art {
    position: absolute;
    inset: 0 0 480px 0;
    background:
      radial-gradient(ellipse 260px 170px at 480px 400px, rgba(247,147,30,0.55), rgba(247,147,30,0) 70%),
      linear-gradient(180deg, #5f86b3 0%, #3e6a9a 55%, rgba(27,74,120,0) 100%);
  }
  .brand {
    position: absolute;
    left: 36px;
    top: 34px;
    display: flex;
    align-items: center;
    gap: 12px;
  }
  .brand-dot {
    width: 34px;
    height: 34px;
    border-radius: 50%;
    background: var(--orange);
  }
  .brand-name {
    font-size: 58px;
    font-weight: 600;
    color: var(--logo-ink);
    letter-spacing: 1px;
    line-height: 1;
  }
  .line {
    position: absolute;
    line-height: 1;
    white-space: nowrap;
  }
  .centered {
    left: 0;
    width: 927px;
    text-align: center;
  }
  .theme {
    left: 450px;
    top: 43px;
    font-size: 24px;
    font-weight: 600;
    letter-spacing: 4px;
    color: var(--mist);
  }
  .title-main {
    left: 20px;
    top: 371px;
    font-size: 258px;
    font-weight: 400;
    color: var(--orange);
    letter-spacing: -7px;
  }
  .title-sub {
    left: 32px;
    top: 600px;
    font-size: 68px;
    font-weight: 400;
  }
  .title-year {
    right: 34px;
    top: 610px;
    font-size: 68px;
    font-weight: 400;
  }
  .focus {
    top: 732px;
    font-size: 67px;
    font-weight: 700;
    color: var(--orange);
  }
  .date { font-size: 33px; font-weight: 600; }
  .date-first { top: 812px; }
  .date-second { top: 852px; }
  .accent { color: var(--orange); }
  .speaker-label {
    top: 899px;
    font-size: 31px;
    font-weight: 600;
    letter-spacing: 10px;
  }
  .speaker {
    top: 941px;
    font-size: 51px;
    font-weight: 600;
  }
  .heading { font-size: 29px; font-weight: 600; }
  .location-heading { top: 1012px; }
  .contact-heading { top: 1092px; }
  .info { font-weight: 600; }
  .address { top: 1047px; font-size: 22px; }
  .contact { top: 1129px; font-size: 21.5px; }
</style>
</head>
<body>
  <main class="flyer">
    <div class="hero-art" role="img" aria-label="Illustration of a white dove in flight over rising flames, open hands and faint crosses against a blue sky with scattered birds"></div>

    <div class="brand">
      <span class="brand-dot"></span>
      <span class="brand-name">HALVERN</span>
    </div>

    <p class="line theme">Tongues of Fire</p>

    <h1 class="line title-main">Harvest</h1>
    <p class="line title-sub">GATHERING</p>
    <p class="line title-year">2018</p>

    <p class="line centered focus">FIRE, REVIVAL, PROPHETIC</p>

    <p class="line centered date date-first">December <span class="accent">28th, 29th @ 7:00PM</span></p>
    <p class="line centered date date-second">December <span class="accent">30th @ 10:00AM</span></p>

    <p class="line centered speaker-label">Speaker</p>
    <p class="line centered speaker">Prophet <span class="accent">Marcus Obuya</span></p>

    <p class="line centered heading location-heading">LOCATION:</p>
    <p class="line centered info address">Lindqvist Community Center, 482 Tamsworth Street, Portland, ME 04102</p>

    <p class="line centered heading contact-heading">CONTACT INFORMATION:</p>
    <p class="line centered info contact">E-mail: contact@cedarbrookfellowship.org - Telephone number: 207 555 0148</p>
  </main>
</body>
</html>
```